Brindlewood Court Apartments Business Cards

We need a business card design for a small apartment community in the metro-Detroit area. The property has a park-like feel and is surrounded by trees and ponds.

The logo colors are:
R=9 G=117 B=127
R=210 G=183 B=114

Contact Information for Business Card

Marla Finch
Property Manager
Brindlewood Court Apartments
352 Brindlewood Way
Lake Orion, MI 48190
Phone (248)517-2039

```html
<!DOCTYPE html>
<html lang="en">
<head>
<meta charset="utf-8">
<title>Brindlewood Court Apartments – Business Cards</title>
<link rel="stylesheet" href="https://fonts.googleapis.com/css2?family=Cinzel:wght@600&family=Lato:wght@300;400&display=swap">
<style>
  :root {
    --page: #d9dadb;
    --card: #1c1c1c;
    --teal: #09757f;
    --gold: #d2b772;
    --text-main: #e6e6e6;
    --text-soft: #a9a9a9;
  }
  html, body {
    margin: 0;
    width: 1200px;
    height: 844px;
    overflow: hidden;
    background: var(--page);
  }
  .sheet {
    position: relative;
    width: 1200px;
    height: 844px;
    display: flex;
    align-items: center;
    justify-content: center;
    gap: 48px;
  }
  .card {
    position: relative;
    width: 532px;
    height: 304px;
    background: var(--card);
    box-shadow: 0 6px 18px rgba(0,0,0,.25);
    box-sizing: border-box;
  }

  /* Back: contact side */
  .card--contact .brand-mark {
    position: absolute;
    left: 34px;
    top: 96px;
    width: 200px;
    height: 120px;
    display: flex;
    align-items: center;
    gap: 12px;
  }
  .brand-mark .sun {
    flex: 0 0 auto;
    width: 46px;
    height: 46px;
    border-radius: 50%;
    background: var(--gold);
  }
  .brand-mark .brand-name {
    font-family: "Cinzel", serif;
    font-weight: 600;
    font-size: 17px;
    line-height: 1.25;
    color: var(--teal);
    letter-spacing: .04em;
  }
  .contact {
    position: absolute;
    left: 282px;
    top: 70px;
    font-family: "Lato", sans-serif;
    color: var(--text-main);
  }
  .contact .person {
    font-size: 19px;
    font-weight: 400;
    margin: 0;
  }
  .contact .role {
    font-size: 13px;
    font-weight: 300;
    color: var(--text-soft);
    margin: 2px 0 16px;
  }
  .contact ul {
    list-style: none;
    margin: 0;
    padding: 0;
  }
  .contact li {
    display: flex;
    align-items: center;
    gap: 9px;
    font-size: 13.5px;
    font-weight: 300;
    line-height: 21px;
  }
  .contact li svg {
    width: 11px;
    height: 11px;
    fill: none;
    stroke: var(--text-main);
    stroke-width: 1.6;
  }

  /* Front: brand side */
  .card--brand {
    display: flex;
    flex-direction: column;
    align-items: center;
    justify-content: center;
  }
  .card--brand .sun {
    width: 54px;
    height: 54px;
    border-radius: 50%;
    background: var(--gold);
    margin-bottom: 22px;
  }
  .card--brand .brand-name {
    font-family: "Cinzel", serif;
    font-weight: 600;
    color: var(--gold);
    text-align: center;
    margin: 0;
    font-size: 26px;
    letter-spacing: .06em;
    line-height: 1.2;
  }
  .card--brand .brand-name span {
    display: block;
    font-size: 12px;
    letter-spacing: .12em;
  }
</style>
</head>
<body>
<main class="sheet">
  <section class="card card--contact">
    <div class="brand-mark">
      <span class="sun"></span>
      <span class="brand-name">Brindlewood Court</span>
    </div>
    <div class="contact">
      <p class="person">Marla Finch</p>
      <p class="role">Managing Director</p>
      <ul>
        <li>
          <svg viewBox="0 0 12 12"><rect x="3" y="1" width="6" height="10" rx="1"/></svg>
          (248)517-2039
        </li>
        <li>
          <svg viewBox="0 0 12 12"><path d="M1 4 Q6 0 11 4 L9 5 L8 3.5 Q6 3 4 3.5 L3 5 Z"/><rect x="2.5" y="6" width="7" height="4.5" rx=".5"/></svg>
          (248)517-2039
        </li>
        <li>
          <svg viewBox="0 0 12 12"><rect x="1" y="2.5" width="10" height="7"/><path d="M1 2.5 L6 7 L11 2.5"/></svg>
          info@brindlewoodcourt.com
        </li>
        <li>
          <svg viewBox="0 0 12 12"><path d="M5 7 L7 5"/><path d="M4.5 5.5 L3 7 A2 2 0 0 0 5 9 L6.5 7.5"/><path d="M7.5 6.5 L9 5 A2 2 0 0 0 7 3 L5.5 4.5"/></svg>
          www.brindlewoodcourt.com
        </li>
      </ul>
    </div>
  </section>

  <section class="card card--brand">
    <span class="sun"></span>
    <h1 class="brand-name">Brindlewood Court<span>Apartments</span></h1>
  </section>
</main>
</body>
</html>
```